Roll label Flyer design

I need a flyer for a roll label printer
Pictures for the project are located here:
https://brindlework.filedrop.example/d-k7mx2291q0a553714

Text I want is located here:
https://brindlework.example/roll-labels.php

Target Market(s)

Manufactures, wholesalers

Industry/Entity Type

Printing

Requirements
Must have
• Lots of pictures. Our phone number 800-472-6018. Website www.brindlework.example

```html
<!DOCTYPE html>
<html lang="en">
<head>
<meta charset="utf-8">
<title>Roll/Product Labels – Brindlework</title>
<link href="https://fonts.googleapis.com/css2?family=Saira:wght@400;500;800&family=Saira+Condensed:wght@600&display=swap" rel="stylesheet">
<style>
  :root{
    --brand-red:#c0121a;
    --deep-red:#a90f16;
    --ink:#1f1f1f;
    --white:#ffffff;
    --steel-light:#e4e6e8;
    --steel-mid:#b9bdc1;
    --steel-dark:#6d7278;
  }
  *{margin:0;padding:0;box-sizing:border-box}
  html,body{width:931px;height:1200px;overflow:hidden;background:var(--white)}
  .flyer{position:relative;width:931px;height:1200px;overflow:hidden;font-family:"Saira",sans-serif;color:var(--ink);background:var(--white)}

  .hero-photo{position:absolute;left:0;top:0;width:931px;height:700px;
    background:linear-gradient(180deg,#b7bbc0 0%,#d9dcdf 35%,#e9ebec 70%,#ffffff 100%);}

  .brand{position:absolute;left:556px;top:48px;display:flex;align-items:center;gap:12px}
  .brand-dot{width:60px;height:60px;border-radius:50%;background:var(--brand-red)}
  .brand-name{font-family:"Saira Condensed",sans-serif;font-weight:600;font-size:32px;letter-spacing:6px;color:var(--white);text-transform:uppercase}

  .headline{position:absolute;left:50px;top:200px;font-weight:800;font-size:35px;color:var(--brand-red);letter-spacing:.3px}
  .intro{position:absolute;left:50px;top:262px;width:318px;font-size:17.5px;line-height:22.4px;text-align:justify;letter-spacing:.5px;color:var(--ink)}

  .press-photo{position:absolute;left:414px;top:204px;width:478px;height:366px;transform:rotate(2.2deg);
    border:6px solid var(--white);box-shadow:0 2px 8px rgba(0,0,0,.25);
    background:linear-gradient(135deg,#cdd0d3 0%,#eef0f1 45%,#9ea3a8 80%,#c9b79a 100%)}
  .press-photo.back{transform:rotate(-1.4deg);left:420px;top:212px;box-shadow:none;background:#f3f3f3}

  .features{position:absolute;left:50px;top:446px;list-style:none}
  .features li{display:flex;align-items:center;height:42.3px;font-size:25px;letter-spacing:.4px}
  .features svg{width:30px;height:30px;margin-right:14px}

  .markets-title{position:absolute;left:0;width:931px;top:684px;text-align:center;font-weight:800;font-size:21.5px;color:var(--brand-red);letter-spacing:.4px}
  .markets{position:absolute;left:118px;top:727px;display:flex;list-style:none}
  .market{width:116px;display:flex;flex-direction:column;align-items:center;text-align:center;font-size:12.5px;line-height:16px;color:var(--brand-red)}
  .market .badge{width:70px;height:70px;border-radius:50%;background:var(--brand-red);display:flex;align-items:center;justify-content:center;margin-bottom:20px}
  .market svg{width:42px;height:42px}

  .gallery-tile{position:absolute;background:linear-gradient(135deg,#5a5f63,#c4c7ca 55%,#3d4145)}
  .tile-rolls{left:6px;top:866px;width:184px;height:328px;background:linear-gradient(180deg,#8a2a22 0%,#cfd1d3 20%,#6f7377 55%,#e2e3e4 80%,#777b7f 100%)}
  .tile-warning{left:198px;top:866px;width:240px;height:158px;background:linear-gradient(120deg,#3a342d,#8a8072 40%,#d23a35 60%,#5b554c)}
  .tile-press{left:446px;top:866px;width:221px;height:158px;background:linear-gradient(90deg,#9fa3a6,#e8eaeb 45%,#3f7fc4 60%,#cfd2d4)}
  .tile-spindle{left:674px;top:866px;width:250px;height:158px;background:linear-gradient(90deg,#cfcab2,#2b2c2e 40%,#121314 70%,#7a7c7e)}
  .tile-foil{left:198px;top:1032px;width:258px;height:162px;background:linear-gradient(150deg,#2c2a26,#a38750 40%,#e8e6e1 70%,#3b3b3d)}

  .contact{position:absolute;left:462px;top:1032px;width:466px;height:162px;background:var(--brand-red);color:var(--white);padding:34px 0 0 18px}
  .contact-line{display:flex;align-items:center;font-weight:800;white-space:nowrap}
  .contact-phone{font-size:35px;letter-spacing:.8px}
  .contact-web{font-size:19.5px;margin-top:12px;letter-spacing:.2px}
  .contact svg{flex:none;margin-right:12px}
</style>
</head>
<body>
<main class="flyer">
  <div class="hero-photo" role="img" aria-label="Label printing plant with roll presses, blurred in the background"></div>

  <div class="brand"><span class="brand-dot"></span><span class="brand-name">Brindlework</span></div>

  <h1 class="headline">Roll/Product Labels</h1>
  <p class="intro">Long or short run. Digital or flexographic. Standard shapes or unique, custom diecuts. Simple spot colors or full color with every embellishment. Let us help you create the perfect label for your application.</p>

  <div class="press-photo back"></div>
  <div class="press-photo" role="img" aria-label="Press operator working at a roll label printing press"></div>

  <ul class="features">
    <li><svg viewBox="0 0 30 30"><path d="M3 16 L11 25 L27 3" fill="none" stroke="var(--brand-red)" stroke-width="3.2" stroke-linecap="round" stroke-linejoin="round"/></svg>Foil-Stamping</li>
    <li><svg viewBox="0 0 30 30"><path d="M3 16 L11 25 L27 3" fill="none" stroke="var(--brand-red)" stroke-width="3.2" stroke-linecap="round" stroke-linejoin="round"/></svg>Embossing</li>
    <li><svg viewBox="0 0 30 30"><path d="M3 16 L11 25 L27 3" fill="none" stroke="var(--brand-red)" stroke-width="3.2" stroke-linecap="round" stroke-linejoin="round"/></svg>Spot Varnishes</li>
    <li><svg viewBox="0 0 30 30"><path d="M3 16 L11 25 L27 3" fill="none" stroke="var(--brand-red)" stroke-width="3.2" stroke-linecap="round" stroke-linejoin="round"/></svg>Instant Redeemable Coupons</li>
    <li><svg viewBox="0 0 30 30"><path d="M3 16 L11 25 L27 3" fill="none" stroke="var(--brand-red)" stroke-width="3.2" stroke-linecap="round" stroke-linejoin="round"/></svg>Expanded Content/Booklet Labels</li>
  </ul>

  <h2 class="markets-title">Specialty Markets We Service Include:</h2>
  <ul class="markets">
    <li class="market"><span class="badge"><svg viewBox="0 0 42 42" fill="var(--white)"><path d="M6 8 L18 8 L16 32 L8 32 Z"/><rect x="21" y="20" width="14" height="14" rx="3"/><rect x="25" y="15" width="6" height="5"/></svg></span>Health &amp; Beauty</li>
    <li class="market"><span class="badge"><svg viewBox="0 0 42 42" fill="none" stroke="var(--white)" stroke-width="3.5" stroke-linecap="round"><path d="M10 8 L33 34"/><path d="M32 8 L9 34"/><path d="M28 6 L36 14"/></svg></span>Food &amp; Beverage</li>
    <li class="market"><span class="badge"><svg viewBox="0 0 42 42" fill="var(--white)"><path d="M5 12 H17 C17 20 14 23 11 23 C8 23 5 20 5 12 Z"/><rect x="10" y="23" width="2" height="9"/><rect x="7" y="32" width="8" height="2"/><path d="M25 4 H29 V12 C33 14 34 17 34 20 V36 H20 V20 C20 17 21 14 25 12 Z"/></svg></span>Wine &amp; Spirits</li>
    <li class="market"><span class="badge"><svg viewBox="0 0 42 42" fill="var(--white)"><path d="M11 18 C11 10 16 6 21 6 C26 6 31 10 31 18 Z"/><rect x="9" y="18" width="24" height="3"/><path d="M4 22 C8 30 14 34 21 34 C28 34 34 30 38 22 L34 20 C30 26 26 29 21 29 C16 29 12 26 8 20 Z"/></svg></span>Industrial Safety<br>&amp; Warning</li>
    <li class="market"><span class="badge"><svg viewBox="0 0 42 42" fill="var(--white)"><path d="M8 17 L26 9 V31 L8 23 Z"/><rect x="10" y="23" width="5" height="10"/><path d="M30 15 L35 12 M30 20 H36 M30 25 L35 28" stroke="var(--white)" stroke-width="2.5" stroke-linecap="round"/></svg></span>Promotional</li>
    <li class="market"><span class="badge"><svg viewBox="0 0 42 42" fill="none" stroke="var(--white)" stroke-width="2.5" stroke-linecap="round"><path d="M29 20 V6 H9 V36 H22"/><path d="M13 12 H25 M13 17 H25 M13 22 H21"/><circle cx="30" cy="30" r="7"/><path d="M27 30 L29.5 32.5 L33.5 27.5"/></svg></span>Compliance</li>
  </ul>

  <div class="gallery-tile tile-rolls" role="img" aria-label="Printed product labels running over press rollers"></div>
  <div class="gallery-tile tile-warning" role="img" aria-label="Red danger warning labels on a press web"></div>
  <div class="gallery-tile tile-press" role="img" aria-label="Close view of press stations with blue printed labels"></div>
  <div class="gallery-tile tile-spindle" role="img" aria-label="Roll of finished black product labels on a spindle"></div>
  <div class="gallery-tile tile-foil" role="img" aria-label="Gold foil and white label rolls on a finishing line"></div>

  <section class="contact">
    <p class="contact-line contact-phone"><svg width="32" height="32" viewBox="0 0 24 24" fill="var(--white)"><path d="M6.6 10.8a15.1 15.1 0 0 0 6.6 6.6l2.2-2.2a1 1 0 0 1 1-.25 11.4 11.4 0 0 0 3.6.57 1 1 0 0 1 1 1V20a1 1 0 0 1-1 1A17 17 0 0 1 3 4a1 1 0 0 1 1-1h3.5a1 1 0 0 1 1 1c0 1.25.2 2.45.57 3.57a1 1 0 0 1-.25 1z"/></svg>800-472-6018</p>
    <p class="contact-line contact-web"><svg width="32" height="32" viewBox="0 0 34 34" fill="none" stroke="var(--white)" stroke-width="2.4" stroke-linecap="round" stroke-linejoin="round"><path d="M10 22 A9 9 0 1 1 22 10"/><path d="M13 18 A4 4 0 1 1 18 13"/><path d="M16 16 L30 21 L24 24 L30 30 L28 32 L22 26 L19 32 Z" fill="var(--white)"/></svg>Website www.brindlework.example</p>
  </section>
</main>
</body>
</html>
```